Grins of Pellbrook - Dental, needs a redesign

Purpose:
Redesign website: http://www.grinsofpellbrook.example/

Sections are important, but for content, we can use existing website or have some placeholder text to fill in later.

Some of the required sections:
About us, contact us, services, our offices, our staff, patient education, patient forms (link to Molavex can be used here), link to friendspace, testimonials

Editability:
We would like to be able to update and edit the content in the future, for small changes

Pictures:
Here is a link to the staff pictures we’d like to use on the website:
https://www.filecrate.example/sh/493kq7zz2tt118p5/BBDRmwLe_uKPi8ZrafQWTGeeb?dl=0
You don't have to use all the pictures; just a few.

friendspace page:
https://www.friendspace.example/Grins-of-Pellbrook-627150384019562

Colors: Calming colors/images for a soothing feeling... to assure the patient that it'll not be that bad.

Target Market(s)

General population

Industry/Entity Type

Dental Clinic

Coding

Coded - Design and coding required

Number of Pages Required

5+ page

Requirements
Must have
• About us, contact us, services, our offices, our staff, patient education, patient forms (link to Molavex can be used here), link to friendspace, testimonials.
• Just create the placeholders for content or use from existing website.
• The staff picture of everyone needs to be on the home page - because that makes it more personal and has received positive feedback from many patients.

```html
<!DOCTYPE html>
<html lang="en">
<head>
<meta charset="utf-8">
<title>Grins of Pellbrook - Dental</title>
<link href="https://fonts.googleapis.com/css2?family=Play:wght@400;700&family=Open+Sans:ital,wght@0,400;0,600;0,700;1,400;1,700&display=swap" rel="stylesheet">
<style>
:root{
  --purple:#b28ff0;
  --purple-dark:#9a74e6;
  --teal:#47ccd8;
  --blue:#5a7ee8;
  --ink:#333;
  --grey:#666;
  --light:#f4f4f4;
  --footer:#333;
  --white:#fff;
}
*{box-sizing:border-box;margin:0;padding:0}
html,body{width:1200px;height:3509px;overflow:hidden}
body{font-family:"Open Sans",Arial,sans-serif;color:var(--ink);background:var(--white);position:relative}
h1,h2,h3,h4{font-weight:400}

/* header */
.site-header{position:absolute;left:0;top:0;width:1200px;height:105px;background:var(--white)}
.brand{position:absolute;left:47px;top:14px;display:flex;align-items:center;gap:16px}
.brand-dot{width:44px;height:44px;border-radius:50%;background:var(--purple)}
.brand-name{font-family:"Play",sans-serif;font-size:30px;line-height:32px;color:#444}
.brand-sub{font-family:"Play",sans-serif;font-size:16px;color:var(--purple-dark);line-height:22px}
.header-info{position:absolute;top:30px;display:flex;gap:12px;align-items:flex-start}
.header-info b{display:block;font-size:14px;color:#444;font-weight:600}
.header-info span{font-size:11px;color:#888}
.main-nav{position:absolute;left:0;top:105px;width:952px;height:63px;background:var(--purple);display:flex;align-items:center;padding-left:47px;white-space:nowrap}
.main-nav-band{position:absolute;left:0;top:105px;width:1200px;height:63px;background:var(--purple)}
.main-nav a{color:var(--white);font-size:12px;font-weight:600;text-decoration:none;padding:0 19px;line-height:63px}
.main-nav a.active{background:var(--purple-dark)}
.appointment{position:absolute;left:952px;top:105px;width:201px;height:63px;background:var(--teal);color:var(--white);padding:12px 18px;font-size:13px;font-weight:700;line-height:18px}
.appointment small{display:block;font-weight:400;font-size:12px}

/* hero */
.hero-photo{position:absolute;left:0;top:168px;width:1200px;height:576px;background:linear-gradient(180deg,#8c6a55 0%,#5a4438 45%,#2a2326 75%,#1d1b1e 100%)}
.features{position:absolute;left:47px;top:639px;width:1106px;height:105px;display:flex}
.feature{flex:1;color:var(--white);padding:16px 14px;position:relative}
.feature h3{font-family:"Play",sans-serif;font-weight:400;font-size:29px;line-height:32px}
.feature p{font-size:15px;line-height:18px}
.feature svg{position:absolute;right:22px;top:20px}
.f-blue{background:var(--blue)}.f-teal{background:var(--teal)}.f-purple{background:var(--purple)}

/* about */
.about-title{position:absolute;left:52px;top:770px;font-family:"Play",sans-serif;font-size:34px;font-weight:400;color:#333}
.about-sub{position:absolute;left:52px;top:815px;font-family:"Play",sans-serif;font-size:23px;color:#888}
.about-photo{position:absolute;left:56px;top:863px;width:323px;height:234px;background:linear-gradient(135deg,#c9c2b8,#e9e6e1 50%,#b28a6e)}
.about-text{position:absolute;left:402px;top:855px;width:751px;font-size:14px;line-height:22px;color:#555}
.about-text p{margin-bottom:22px}

/* dental health */
.health{position:absolute;left:0;top:1170px;width:1200px;height:414px;background:var(--teal)}
.health h2{position:absolute;top:34px;width:100%;text-align:center;font-family:"Play",sans-serif;font-weight:400;font-size:36px;letter-spacing:1px;color:var(--white)}
.health-item{position:absolute;top:112px;width:244px;height:257px;color:var(--white);text-align:center}
.health-item svg{margin-top:40px}
.health-item p{font-family:"Play",sans-serif;font-size:20px;margin-top:34px}
.health-item.active{border:2px solid var(--white)}

/* team */
.team-title{position:absolute;top:1620px;width:1200px;text-align:center;font-family:"Play",sans-serif;font-size:38px;font-weight:400;color:#333}
.team-sub{position:absolute;top:1667px;width:1200px;text-align:center;font-size:14px;color:#888}
.staff-card{position:absolute;top:1726px;width:332px;height:309px;background:#eee}
.staff-photo{width:332px;height:234px;background:linear-gradient(180deg,#a44b3a,#8a3d30 60%,#4a2b2a)}
.staff-card h4{font-family:"Play",sans-serif;font-weight:400;font-size:20px;text-align:center;margin-top:14px;color:#333}
.staff-card span{display:block;text-align:center;font-size:14px;color:var(--purple-dark)}
.arrow{position:absolute;top:1860px}
.divider{position:absolute;left:0;top:2096px;width:1200px;height:5px;background:linear-gradient(90deg,var(--blue),var(--teal) 40%,var(--purple))}

/* testimonial */
.testimonial{position:absolute;left:0;top:2101px;width:1200px;height:416px;background:var(--light)}
.couple-photo{position:absolute;left:47px;top:2133px;width:451px;height:384px;background:linear-gradient(160deg,#e8f0f6,#bcd3e6 55%,#d8b8a2)}
.t-title{position:absolute;left:515px;top:2153px;font-family:"Play",sans-serif;font-size:28px;font-weight:400;color:#333}
.quote-mark{position:absolute;left:488px;top:2195px;font-size:46px;color:#555;font-family:Georgia,serif}
.t-text{position:absolute;left:515px;top:2212px;width:640px;font-size:14px;line-height:23px;font-style:italic;color:#888}
.t-text p{margin-bottom:22px}
.t-name{position:absolute;left:515px;top:2385px;font-size:17px;font-weight:700;font-style:italic;color:#333}
.t-role{position:absolute;left:515px;top:2408px;font-size:17px;font-style:italic;color:#666}
.dots{position:absolute;left:532px;top:2452px;display:flex;gap:6px}
.dots i{width:18px;height:18px;border-radius:50%;background:#aaa}
.dots i.on{background:var(--teal)}

/* cta */
.cta{position:absolute;left:0;top:2517px;width:1200px;height:164px;background:var(--purple)}
.cta svg{position:absolute;left:50px;top:38px}
.cta h2{position:absolute;left:152px;top:28px;font-family:"Play",sans-serif;font-size:36px;font-weight:700;color:var(--white)}
.cta p{position:absolute;left:152px;top:76px;width:720px;font-size:16px;line-height:22px;color:var(--white)}
.cta-btn{position:absolute;left:929px;top:51px;width:224px;height:61px;border:2px solid var(--white);color:var(--white);font-size:15px;text-align:center;line-height:57px}

/* map */
.map{position:absolute;left:0;top:2681px;width:1200px;height:372px;background:linear-gradient(135deg,#e4e0f2,#d4cdf0 50%,#e8e6f1)}

/* footer */
.site-footer{position:absolute;left:0;top:3053px;width:1200px;height:397px;background:var(--footer);color:#ccc}
.f-brand{position:absolute;left:56px;top:47px;display:flex;align-items:center;gap:10px}
.f-brand .brand-dot{width:32px;height:32px;background:#777}
.f-brand b{font-family:"Play",sans-serif;font-size:22px;color:var(--white);font-weight:400;display:block;line-height:24px}
.f-brand small{font-size:11px;color:#aaa}
.f-about{position:absolute;left:56px;top:103px;width:330px;font-size:14px;line-height:22px}
.f-contact{position:absolute;left:56px;top:172px;list-style:none;font-size:14px}
.f-contact li{display:flex;align-items:center;gap:18px;height:32px}
.f-title{position:absolute;top:37px;font-family:"Play",sans-serif;font-size:28px;font-weight:400;color:#eee}
.f-title::after{content:"";display:block;width:118px;height:2px;background:var(--teal);margin-top:8px}
.news-note{position:absolute;left:451px;top:106px;width:250px;font-size:13px;line-height:19px;display:flex;gap:8px}
.news-input{position:absolute;left:447px;width:243px;height:38px;border-radius:19px;background:var(--white);color:#333;font-size:13px;padding:10px 18px}
.news-btn{position:absolute;left:447px;top:280px;width:124px;height:40px;border-radius:20px;background:var(--teal);color:#123;font-size:14px;text-align:center;line-height:40px}
.hours{position:absolute;left:784px;top:105px;width:340px;list-style:none;font-size:14px}
.hours li{display:flex;align-items:center;height:26px}
.hours li i{width:12px;height:12px;border:2px solid var(--teal);border-radius:50%;margin-right:14px}
.hours li span{margin-left:auto}
.social{position:absolute;left:903px;top:330px;display:flex;gap:10px}
.social a{width:36px;height:36px;background:#1da4e0;display:block}
.copyright{position:absolute;left:0;top:3450px;width:1200px;height:59px;background:var(--purple);color:var(--white);text-align:center;line-height:59px;font-size:16px}
</style>
</head>
<body>

<header class="site-header">
  <div class="brand">
    <div class="brand-dot"></div>
    <div>
      <div class="brand-name">Dr. Meera Anand, DDS</div>
      <div class="brand-sub">Grins of Pellbrook</div>
    </div>
  </div>
  <div class="header-info" style="left:603px">
    <svg width="30" height="30" viewBox="0 0 30 30" fill="var(--teal)"><circle cx="5" cy="5" r="3"/><circle cx="15" cy="5" r="3"/><circle cx="25" cy="5" r="3"/><circle cx="5" cy="15" r="3"/><circle cx="15" cy="15" r="3"/><circle cx="25" cy="15" r="3"/><circle cx="5" cy="25" r="3"/><circle cx="15" cy="25" r="3"/><circle cx="25" cy="25" r="3"/></svg>
    <div><b>Call Today 020 7946 0321</b><span>42 Holloway Lane, Pellbrook W7 5QT</span></div>
  </div>
  <div class="header-info" style="left:896px">
    <svg width="32" height="32" viewBox="0 0 32 32" fill="none" stroke="var(--teal)" stroke-width="2.5"><circle cx="16" cy="16" r="13"/><path d="M16 8v8l6 4"/></svg>
    <div><b>Open Hours</b><span>Mon - Sat: 8 am - 5 pm, Sunday: CLOSED</span></div>
  </div>
</header>

<div class="main-nav-band"></div>
<nav class="main-nav">
  <a class="active" href="#">ABOUT US</a><a href="#">CONTACT US</a><a href="#">SERVICES</a><a href="#">OUR OFFICES</a><a href="#">OUR STAFF</a><a href="#">PATIENT EDUCATION</a><a href="#">PATIENT FORMS</a>
</nav>
<div class="appointment">MAKE AN APPOINTMENT<small>It's so fast</small></div>

<div class="hero-photo" role="img" aria-label="Group photo of the five dental team members seated in front of a stone fireplace"></div>
<div class="features">
  <div class="feature f-blue">
    <h3>Dental Implants</h3><p>Pre-order today just for $879 per tooth</p>
    <svg width="54" height="62" viewBox="0 0 54 62" fill="none" stroke="#fff" stroke-width="2.5"><path d="M10 4h34c2 6-2 12-6 12H16c-4 0-8-6-6-12z"/><path d="M16 22h22M18 30h18M20 38h14M22 46h10M25 54h4"/></svg>
  </div>
  <div class="feature f-teal">
    <h3>Cosmetic Braces</h3><p>Affordable french braces for<br>kids and adults</p>
    <svg width="56" height="62" viewBox="0 0 56 62" fill="none" stroke="#fff" stroke-width="2.5"><path d="M28 3l22 8v18c0 15-10 25-22 30C16 54 6 44 6 29V11z"/><path d="M20 22c3-3 5-1 8-1s5-2 8 1c3 3 0 9-1 13-1 3-2 6-3 6s-1-5-4-5-3 5-4 5-2-3-3-6c-1-4-4-10-1-13z"/></svg>
  </div>
  <div class="feature f-purple">
    <h3>Teeth Whitening</h3><p>Top standards and high quality</p>
    <svg width="56" height="62" viewBox="0 0 56 62" fill="none" stroke="#fff" stroke-width="2.5"><path d="M18 14c-7 0-11 5-11 12 0 7 4 10 5 18 1 7 2 14 5 14s4-10 8-10 5 10 8 10 4-7 5-14c1-8 5-11 5-18 0-7-4-12-11-12-4 0-6 2-7 2s-3-2-7-2z"/><path d="M46 4v8M42 8h8M10 2v6M7 5h6"/></svg>
  </div>
</div>

<h1 class="about-title">About Us</h1>
<div class="about-sub">Meera Anand, DDS</div>
<div class="about-photo" role="img" aria-label="Dentist in a white coat treating a seated patient"></div>
<div class="about-text">
  <p>Dr. Meera Anand provides a full range of dental services to the whole family. Many of our patient families span multiple generations. Our Team are dedicated to taking the time needed to provide the very best care every patient deserves.</p>
  <p>Please tour our web site to learn more about family dentistry, cosmetic dentistry and our restorative dental services. We invite you to call us with any questions you may have - we all look forward to meeting you and your family!</p>
  <p>New patients looking for quality dental care in a relaxed environment are welcome! We accept PPO, Indeminity and Traditional Insurance plans.</p>
</div>

<section class="health">
  <h2>DENTAL HEALTH</h2>
  <div class="health-item active" style="left:56px;top:110px">
    <svg width="110" height="110" viewBox="0 0 110 110" fill="#fff"><path d="M34 30c-13 0-20 9-20 22 0 12 7 18 9 31 2 12 4 24 9 24s7-16 14-16 9 16 14 16 7-12 9-24c2-13 9-19 9-31 0-13-7-22-20-22-8 0-11 4-12 4s-4-4-12-4z"/><g fill="none" stroke="#fff" stroke-width="2.5"><circle cx="80" cy="16" r="6"/><circle cx="96" cy="28" r="5"/><circle cx="70" cy="34" r="4"/><circle cx="88" cy="46" r="4"/><circle cx="100" cy="10" r="3"/></g></svg>
    <p>General Dental Health</p>
  </div>
  <div class="health-item" style="left:356px">
    <svg width="110" height="110" viewBox="0 0 110 110" fill="none" stroke="#fff" stroke-width="3"><text x="40" y="72" fill="#fff" stroke="none" font-family="Play,sans-serif" font-size="44">?</text><path d="M40 40L22 22M70 40l18-18M40 70L22 88M70 70l18 18M30 55H10M80 55h20"/><circle cx="18" cy="18" r="6"/><circle cx="92" cy="18" r="6"/><circle cx="18" cy="92" r="6"/><circle cx="92" cy="92" r="6"/><circle cx="6" cy="55" r="5"/><circle cx="104" cy="55" r="5"/></svg>
    <p>Dental FAQ</p>
  </div>
  <div class="health-item" style="left:601px">
    <svg width="110" height="110" viewBox="0 0 110 110"><path fill="#fff" d="M30 12c-13 0-20 9-20 22 0 12 7 18 9 31 2 12 4 24 9 24s7-16 14-16 9 16 14 16 7-12 9-24c2-13 9-19 9-31 0-13-7-22-20-22-8 0-11 4-12 4s-4-4-12-4z"/><circle cx="62" cy="50" r="16" fill="var(--teal)" stroke="#fff" stroke-width="5"/><path d="M74 62l22 22" stroke="#fff" stroke-width="8" stroke-linecap="round"/></svg>
    <p>Cosmetic Dentistry</p>
  </div>
  <div class="health-item" style="left:846px">
    <svg width="110" height="110" viewBox="0 0 110 110"><path fill="#fff" d="M26 38c-12 0-18 8-18 19 0 10 6 15 8 26 2 10 3 20 8 20s6-14 12-14 8 14 12 14 6-10 8-20c2-11 8-16 8-26 0-11-6-19-18-19-7 0-9 3-10 3s-3-3-10-3z"/><path d="M62 46L88 8l10 6-22 40" fill="#fff"/><path d="M92 12l8-8" stroke="#fff" stroke-width="4"/></svg>
    <p>Advanced Procedures</p>
  </div>
</section>

<h2 class="team-title">Our Dental Team</h2>
<div class="team-sub">Professional and highly trained</div>
<svg class="arrow" style="left:24px" width="20" height="36" viewBox="0 0 20 36" fill="none" stroke="#555" stroke-width="2"><path d="M18 2L2 18l16 16"/></svg>
<div class="staff-card" style="left:73px">
  <div class="staff-photo" role="img" aria-label="Portrait of Dr. Meera Anand against a brick wall"></div>
  <h4>Dr. Meera Anand</h4><span>Dentist</span>
</div>
<div class="staff-card" style="left:433px">
  <div class="staff-photo" role="img" aria-label="Portrait of Carla Denholm against a brick wall"></div>
  <h4>Carla Denholm</h4><span>Dentist</span>
</div>
<div class="staff-card" style="left:793px">
  <div class="staff-photo" role="img" aria-label="Portrait of a team member against a brick wall"></div>
  <h4>Dr. Meera Anand</h4><span>Dentist</span>
</div>
<svg class="arrow" style="left:1156px" width="20" height="36" viewBox="0 0 20 36" fill="none" stroke="#555" stroke-width="2"><path d="M2 2l16 16L2 34"/></svg>
<div class="divider"></div>

<section class="testimonial"></section>
<div class="couple-photo" role="img" aria-label="Smiling older couple embracing"></div>
<h3 class="t-title">PATIENT SAYS</h3>
<div class="quote-mark">&ldquo;</div>
<div class="t-text">
  <p>Dr. Meera Anand provides a full range of dental services to the whole family. Many of our patient families span multiple generations. Our Team are dedicated to taking the time needed to provide the very best care every patient deserves.</p>
  <p>Please tour our web site to learn more about family dentistry, cosmetic dentistry and our restorative dental services. We invite you to call us with any questions you may have - we all look forward to meeting you and your family!</p>
</div>
<div class="t-name">Rosalind Petrie</div>
<div class="t-role">Patient</div>
<div class="dots"><i class="on"></i><i></i><i></i></div>

<section class="cta">
  <svg width="70" height="88" viewBox="0 0 70 88" fill="none" stroke="#fff" stroke-width="3"><path d="M8 4h54c3 10-3 18-9 18H17C11 22 5 14 8 4z"/><path d="M16 32h38M19 44h32M22 56h26M26 68h18M31 80h8"/></svg>
  <h2>Your Perfect Smile is Just a Click Away!</h2>
  <p>Lorem ipsum dolor sit amet, consectetuer adipiscing elit. Aenean commodo ligula eget dolor. Aenean massa. Cum sociis natoque penatibus et magnis dis parturient montes</p>
  <div class="cta-btn">BOOK APPOINTMENT</div>
</section>

<div class="map" role="img" aria-label="Street map showing the clinic location with a purple marker"></div>

<footer class="site-footer">
  <div class="f-brand"><div class="brand-dot"></div><div><b>Dr. Meera Anand, DDS</b><small>Grins of Pellbrook</small></div></div>
  <p class="f-about">Dr. Meera Anand provides a full range of dental services to the whole family. Many of our patient families span multiple.</p>
  <ul class="f-contact">
    <li><svg width="16" height="20" viewBox="0 0 16 20" fill="var(--teal)"><path d="M8 0a7 7 0 0 0-7 7c0 5 7 13 7 13s7-8 7-13a7 7 0 0 0-7-7zm0 10a3 3 0 1 1 0-6 3 3 0 0 1 0 6z"/></svg>1180 Marrow Street, Suite 2C</li>
    <li><svg width="16" height="18" viewBox="0 0 16 18" fill="var(--teal)"><path d="M3 0l3 4-2 2c1 3 3 5 6 7l2-2 4 3-2 4C7 18 0 10 0 3z"/></svg>309-555-0142/0143</li>
    <li><svg width="18" height="14" viewBox="0 0 18 14" fill="none" stroke="var(--teal)" stroke-width="2"><rect x="1" y="1" width="16" height="12"/><path d="M1 1l8 7 8-7"/></svg>info@grinsofpellbrook.example</li>
    <li><svg width="18" height="16" viewBox="0 0 18 16" fill="none" stroke="var(--teal)" stroke-width="2"><rect x="1" y="1" width="16" height="14"/><path d="M1 5h16"/></svg>www.grinsofpellbrook.example</li>
  </ul>

  <h4 class="f-title" style="left:451px">Newsletter</h4>
  <div class="news-note"><svg width="16" height="14" viewBox="0 0 16 14" fill="#fff"><path d="M0 2h16v10H0z"/></svg><span>Sign up with your name and email to get updates fresh updates</span></div>
  <div class="news-input" style="top:172px">Name</div>
  <div class="news-input" style="top:225px">Email</div>
  <div class="news-btn">Subscribe</div>

  <h4 class="f-title" style="left:784px">Opening Hours</h4>
  <ul class="hours">
    <li><i></i>Monday<span>8:00 AM - 9:00 PM</span></li>
    <li><i></i>Tuesday<span>8:00 AM - 9:00 PM</span></li>
    <li><i></i>Wednesday<span>8:00 AM - 9:00 PM</span></li>
    <li><i></i>Thursday<span>8:00 AM - 9:00 PM</span></li>
    <li><i></i>Friday<span>8:00 AM - 9:00 PM</span></li>
    <li><i></i>Saturday<span>9:00 AM - 6:00 PM</span></li>
    <li><i></i>Sunday<span>CLOSED</span></li>
  </ul>
  <div class="social">
    <a href="https://www.friendspace.example/Grins-of-Pellbrook-627150384019562" aria-label="friendspace"></a>
    <a href="#" aria-label="Social link"></a>
    <a href="#" aria-label="Social link"></a>
    <a href="#" aria-label="Social link"></a>
    <a href="#" aria-label="Social link"></a>
  </div>
</footer>
<div class="copyright">Copyright © 2015 Grins Of Pellbrook</div>

</body>
</html>
```